Book Flyer

I want a flyer that we can use to promote this book to educators and to leaders....below is a sample flyer but I want something bold and creative and different from this....it can be completely different from what is attached. I want to be a WOW to increase sales. Please include pic of book and how folks can get a copy....I've given you a few pics but please be creative ....looking for a wow.

```html
<!DOCTYPE html>
<html lang="en">
<head>
<meta charset="utf-8">
<title>Purposeful Momentum – Book Flyer</title>
<link href="https://fonts.googleapis.com/css2?family=Roboto+Condensed:wght@300;400;700&family=Oswald:wght@500;600&family=Mulish:wght@700;800&family=Questrial&display=swap" rel="stylesheet">
<style>
  :root{
    --red:#e31e24;
    --red-dark:#b5161b;
    --red-deep:#9e1418;
    --yellow:#fdc70c;
    --green:#8cc63f;
    --blue:#00aeef;
    --grey:#d3d2d2;
    --ink:#111111;
    --white:#ffffff;
    --page:#ececec;
    --suit:#2c2f3a;
  }
  *{box-sizing:border-box;margin:0;padding:0}
  html,body{width:1200px;height:1200px;overflow:hidden;background:var(--page)}
  .flyer{
    position:absolute;left:211px;top:50px;width:945px;height:1335px;
    transform:scale(0.8231);transform-origin:0 0;overflow:hidden;
    background:var(--red);
    box-shadow:0 4px 18px rgba(0,0,0,.18);
  }
  .flyer__backdrop{position:absolute;inset:0;width:945px;height:1335px}
  .title{position:absolute;left:40px;top:88px;width:512px;text-align:right;white-space:nowrap;
    font-family:"Oswald",sans-serif;font-weight:600;line-height:1;text-shadow:3px 3px 0 rgba(90,0,0,.55)}
  .title__main{display:block;color:var(--white);font-size:94px;letter-spacing:0}
  .title__sub{display:block;color:var(--yellow);font-size:78px;margin-top:8px;letter-spacing:1px}
  .book-cover{position:absolute;left:595px;top:58px;width:315px;height:250px;
    background:linear-gradient(160deg,#1d2b4f 0 42%,var(--red) 42% 62%,#f4f4f4 62%);
    transform:rotate(-5deg);box-shadow:6px 8px 14px rgba(0,0,0,.35)}
  .endorsement{position:absolute;left:45px;top:338px;width:853px;
    font-family:"Roboto Condensed",sans-serif;font-weight:300;font-size:20.5px;line-height:25.5px;
    letter-spacing:-.3px;color:var(--white);text-align:justify}
  .endorsement__author{position:absolute;right:47px;top:462px;
    font-family:"Roboto Condensed",sans-serif;font-weight:300;font-size:22px;color:var(--white)}
  .strategies-heading{position:absolute;left:55px;top:478px;
    font-family:"Oswald",sans-serif;font-weight:500;font-size:41px;line-height:46px;color:var(--white);
    transform:scaleX(.88);transform-origin:0 0}
  .strategy{position:absolute;width:501px;height:151px;border-radius:8px;padding:20px 24px 0 30px;
    font-family:"Mulish",sans-serif;color:var(--ink);box-shadow:3px 3px 6px rgba(0,0,0,.2)}
  .strategy--equity{left:45px;top:573px;background:var(--yellow)}
  .strategy--change{left:47px;top:735px;background:var(--green);padding-left:24px;padding-right:40px}
  .strategy--communication{left:47px;top:898px;background:var(--blue);padding-left:18px;padding-right:40px}
  .strategy__name{font-family:"Mulish",sans-serif;font-weight:800;font-size:27px;letter-spacing:.5px;line-height:1.1}
  .strategy__quote{font-weight:700;font-size:19.5px;line-height:23px;margin-top:6px}
  .strategy--communication .strategy__quote{line-height:28px}
  .strategy__source{font-weight:800;font-size:18.5px;text-align:right;margin-top:5px;padding-right:0}
  .strategy--change .strategy__source{margin-top:13px;padding-right:0}
  .strategy--communication .strategy__source{margin-top:0;padding-right:36px}
  .author-photo{position:absolute;left:560px;top:530px;width:385px;height:805px;
    background:linear-gradient(180deg,rgba(44,47,58,0) 0%,#3a3d48 18%,var(--suit) 60%,#24262e 100%)}
  .about{position:absolute;left:50px;top:1062px;width:430px}
  .about__heading{font-family:"Questrial",sans-serif;font-size:44px;color:var(--ink);line-height:1.1}
  .about__body{font-family:"Questrial",sans-serif;font-size:18.5px;line-height:19px;color:var(--ink);
    text-align:justify;margin-top:10px}
  .contact{position:absolute;left:568px;top:1237px;width:377px;height:60px;border-radius:10px 0 0 0;
    background:var(--red);color:var(--white);font-family:"Mulish",sans-serif;font-weight:800;
    font-size:26px;line-height:60px;padding-left:24px;white-space:nowrap}
</style>
</head>
<body>
<main class="flyer">
  <svg class="flyer__backdrop" viewBox="0 0 945 1335" aria-hidden="true">
    <rect width="945" height="1335" fill="var(--red)"/>
    <polygon points="0,0 945,0 945,120 420,360 0,240" fill="var(--red-dark)" opacity=".55"/>
    <polygon points="0,0 500,0 0,200" fill="var(--red-deep)" opacity=".6"/>
    <polygon points="600,300 945,150 945,620" fill="var(--red-dark)" opacity=".35"/>
    <polygon points="0,700 945,1070 945,1335 0,1335" fill="var(--grey)"/>
  </svg>

  <h1 class="title">
    <span class="title__main">PURPOSEFUL</span>
    <span class="title__sub">MOMENTUM</span>
  </h1>

  <div class="book-cover" role="img" aria-label="Two copies of the book Purposeful Momentum by S. Marcus Reed, foreword by Alan Whitford"></div>

  <p class="endorsement">“Purposeful Momentum is a book written for all leaders. Dr. Marcus Reed speaks from real life experiences that are relatable and from the heart. His leadership steps have helped him develop into one of the most accomplished administrative leaders in the country. The three specific strategies outlined in the book will transform your leader ship skills and help you stay on track to ensure success”.</p>
  <p class="endorsement__author">Laura Pendleton, Principal</p>

  <h2 class="strategies-heading">3 FUNDAMENTAL STRATEGIES<br>THAT DRIVE LEADERSHIP</h2>

  <div class="author-photo" role="img" aria-label="Photo of the author in a dark suit, reading a copy of the book"></div>

  <section class="strategy strategy--equity">
    <h3 class="strategy__name">EQUITY</h3>
    <p class="strategy__quote">Fairness does not mean everyone gets the same Fairness means everyone gets what they need,”</p>
    <p class="strategy__source">Rick Redmond</p>
  </section>
  <section class="strategy strategy--change">
    <h3 class="strategy__name">CHANGE</h3>
    <p class="strategy__quote">“If you do not change direction, you may end up where you are heading.”</p>
    <p class="strategy__source">Mei Lin Hart</p>
  </section>
  <section class="strategy strategy--communication">
    <h3 class="strategy__name">COMMUNICATION</h3>
    <p class="strategy__quote">“The single biggest problem in communication is the illusion that is has taken place.”</p>
    <p class="strategy__source">Gerald B. Shore</p>
  </section>

  <section class="about">
    <h2 class="about__heading">About Dr. Reed</h2>
    <p class="about__body">Distinguished as a vibrant, visionary, and innovative leader who recocognizes that humility is the most important trait a leader can proses, Dr. Reed uses his prior experiences in business, education, and non profit to assist organization leaders from all industries build internal leadership capacity, including strategy &amp;talent management organizational potential and success.</p>
  </section>

  <p class="contact">info@thereedgroup.com</p>
</main>
</body>
</html>
```